Finch Haulage Ltd

We need an A5 size (UK size) flyer to advertise our new business which is called Finch Haulage.
Domestic and Commercial Waste Clearance Services.
Please have the question in bold "Do you have a pile of junk you need to dispose of?"
We collect all kinds of junk or rubbish from homes and businesses across Kent, Sussex and South London.
No fuss, no mess!
A low cost, hassle free alternative to skip hire.
Licensed by the Landcare Board and fully insured (this can be in small print at the bottom).
Please put the Recycle symbol somewhere.
Our tagline on our vehicle is "We Clear More, For Less!"
We'd like the flyer to be bold and eye-catching (to catch the eye of the homeowner or business owner while it's sitting on their doormat).
We need our telephone, website and email to be prominent. Maybe saying "Call today for a free quote"
Tel. 01734 586019
Email: info@finchhaulage.example.co.uk
www.finchhaulage.example.co.uk
Target Market(s)
Our market will be homes and small businesses around Kent, Sussex and South London.

```html
<!DOCTYPE html>
<html lang="en">
<head>
<meta charset="utf-8">
<title>Finch Haulage – Waste Clearance Flyer</title>
<link rel="stylesheet" href="https://fonts.googleapis.com/css2?family=Fredoka:wght@600;700&display=swap">
<style>
  :root {
    --green-light: #62c93c;
    --green-mid: #3ea62a;
    --green-dark: #1c6e17;
    --green-brand: #3fbf1f;
    --white: #ffffff;
    --ink: #2a2f31;
    --logo-grey: #4a5357;
  }
  * { margin: 0; padding: 0; box-sizing: border-box; }
  html, body { width: 846px; height: 1200px; overflow: hidden; background: var(--white); }
  .flyer {
    position: relative;
    width: 846px;
    height: 1200px;
    font-family: "Fredoka", "Arial Rounded MT Bold", sans-serif;
    font-weight: 700;
    color: var(--white);
    text-align: center;
    overflow: hidden;
  }
  .hero {
    position: absolute;
    top: 0; left: 0;
    width: 846px;
    height: 370px;
    background:
      linear-gradient(to bottom, rgba(0,0,0,0) 78%, rgba(5,30,5,0.85) 100%),
      radial-gradient(ellipse 70% 80% at 50% 45%, var(--green-light) 0%, var(--green-mid) 45%, var(--green-dark) 100%);
  }
  .hero-question {
    position: absolute;
    top: 38px; left: 0;
    width: 100%;
    font-size: 46px;
    font-weight: 700;
    line-height: 70px;
  }
  .hero-question .emphasis {
    color: var(--ink);
    text-shadow: -2px -2px 0 var(--white), 2px -2px 0 var(--white), -2px 2px 0 var(--white), 2px 2px 0 var(--white);
  }
  .recycle-icon {
    position: absolute;
    top: 12px; left: 738px;
    width: 92px; height: 92px;
  }
  .brand-band {
    position: absolute;
    top: 370px; left: 0;
    width: 846px;
    height: 344px;
    background: var(--white);
    padding-top: 30px;
  }
  .brand-name {
    font-size: 84px;
    line-height: 92px;
    color: var(--logo-grey);
  }
  .tagline {
    margin-top: 4px;
    font-size: 32px;
    line-height: 40px;
    color: var(--green-brand);
  }
  .call-line {
    margin-top: 22px;
    font-size: 38px;
    line-height: 46px;
    color: var(--logo-grey);
  }
  .call-line .phone { color: var(--green-brand); }
  .web-line {
    margin-top: 14px;
    font-size: 23px;
    line-height: 30px;
    font-weight: 600;
    color: var(--logo-grey);
  }
  .services {
    position: absolute;
    top: 714px; left: 0;
    width: 846px;
    height: 486px;
    background:
      linear-gradient(to bottom, rgba(5,30,5,0.55) 0%, rgba(0,0,0,0) 8%),
      radial-gradient(ellipse 75% 70% at 50% 40%, var(--green-light) 0%, var(--green-mid) 45%, var(--green-dark) 100%);
  }
  .services-copy {
    position: absolute;
    top: 52px; left: 30px;
    width: 786px;
    font-size: 46px;
    line-height: 70px;
  }
  .services-copy .dark { color: var(--ink); }
  .licence-note {
    position: absolute;
    bottom: 22px; left: 0;
    width: 100%;
    font-family: Arial, Helvetica, sans-serif;
    font-weight: 700;
    font-size: 20px;
  }
</style>
</head>
<body>
<main class="flyer">
  <section class="hero">
    <h1 class="hero-question">Do<br>you have<br>a pile of junk<br>you need to <span class="emphasis">dispose</span> of?</h1>
    <svg class="recycle-icon" viewBox="0 0 100 100" role="img" aria-label="Recycle symbol">
      <defs>
        <g id="chasing-arrow">
          <path d="M28 80 L62 80" fill="none" stroke="#111111" stroke-width="16" stroke-linecap="round"/>
          <path d="M28 80 L62 80" fill="none" stroke="#ffffff" stroke-width="7" stroke-linecap="round"/>
          <polygon points="60,68 78,80 60,92" fill="#111111"/>
          <polygon points="63,74 72,80 63,86" fill="#ffffff"/>
        </g>
      </defs>
      <use href="#chasing-arrow"/>
      <use href="#chasing-arrow" transform="rotate(120 50 57)"/>
      <use href="#chasing-arrow" transform="rotate(240 50 57)"/>
    </svg>
  </section>

  <section class="brand-band">
    <p class="brand-name">Finch Haulage</p>
    <p class="tagline">We Clear More, For Less!</p>
    <p class="call-line">Call today for a free quote: <span class="phone">01734 586019</span></p>
    <p class="web-line">info@finchhaulage.example.co.uk &nbsp;|&nbsp; www.finchhaulage.example.co.uk</p>
  </section>

  <section class="services">
    <p class="services-copy">
      We collect all kinds of junk or rubbish from homes and business.<br>
      No <span class="dark">fuss</span>, no <span class="dark">mess</span>!<br>
      Very competitive prices.
    </p>
    <p class="licence-note">Licensed by the Landcare Board and fully insured</p>
  </section>
</main>
</body>
</html>
```